KV Group

We need a new website for our company and since we had a very good work done for our logo in this site, we're back for the entire job.

Our company name is Marlowe Capital Group. We're adding files of examples of what we have done today. In my opinion we need a more attention lock in the site but yet financial simple work.

Our files (attached) will let you know what we have so far. We need a complete change but the colours should be the same, however you can change them not running away to far from the original, and of course matching with the logo.

We need examples for 3 kind of layouts.

- A HOME welcome layout
- An internal Layout with sidebar
- And internal Layout wide

We can buy image licenses if needed for assets.
Actually there are 5 slide images placed on the Welcome HOME, we need those there, but you can improve with better images to match the new website!!!

Target Market(s)

Clients looking for financial advisers, tax and funds specialist, currency advisers

Industry/Entity Type

Financial

Requirements
Must have
• all the fonts must be in accordance with the financial market sites........the welcome home page must be precise, neat and information accurate........the menu should be elegant........main focus on the Home page, should be also the PRIVATE ACCESS box log in.......

```html
<!DOCTYPE html>
<html lang="en">
<head>
<meta charset="utf-8">
<title>Marlowe Capital Group</title>
<link rel="stylesheet" href="https://fonts.googleapis.com/css2?family=Montserrat:wght@400;700&family=Arimo:wght@400;700&display=swap">
<style>
:root{
  --orange:#f26d21;
  --orange-dark:#c9461a;
  --ink:#333333;
  --text:#555555;
  --page:#f1ece6;
  --white:#ffffff;
  --footer:#535353;
  --footer-deep:#3b3b3b;
  --blue:#1ba2e3;
  --green:#1e9a4a;
  --red:#d0201f;
  --badge:#c8c2ba;
  --badge-dark:#a9a299;
}
*{box-sizing:border-box;margin:0;padding:0}
html,body{width:984px;height:1200px;overflow:hidden;background:var(--page)}
body{font-family:"Arimo",Arial,sans-serif;color:var(--text)}
.site{position:absolute;left:0;top:0;width:1200px;height:1464px;transform:scale(.82);transform-origin:0 0;background:var(--page)}
.abs{position:absolute}
.topline{left:0;top:0;width:1200px;height:4px;background:#2a1a14}
.header{left:0;top:4px;width:1200px;height:113px;background:linear-gradient(#fff,#f3f3f3)}
.brand{left:282px;top:22px;display:flex;align-items:center;gap:8px}
.brand-mark{width:22px;height:22px;background:var(--orange)}
.brand-name{font:700 13px "Montserrat",sans-serif;color:var(--ink);letter-spacing:.5px;text-transform:uppercase;line-height:1.2;width:110px}
.apply{left:807px;top:29px;width:114px;height:30px;background:var(--orange);color:#fff;font:700 9px "Arimo",sans-serif;display:flex;align-items:center;justify-content:center;letter-spacing:.3px;border:1px solid var(--orange-dark)}
.nav{left:258px;top:88px;width:683px;height:29px;display:flex;background:linear-gradient(#fff,#f0f0f0);border-top:1px solid #e4e4e4}
.nav a{flex:auto;display:flex;align-items:center;justify-content:center;font:700 8px "Arimo",sans-serif;color:#222;text-decoration:none;border-right:1px solid #e2e2e2;text-transform:uppercase}
.nav a:last-child{border-right:0}
.nav a.active{border-bottom:3px solid var(--orange)}
.nav a .caret{color:var(--orange);margin-left:3px}
.hero{left:0;top:117px;width:1200px;height:354px;background:linear-gradient(180deg,#4a4846 0%,#5a5048 40%,#3a2c22 75%,#2a2420 100%)}
.hero-title{left:259px;top:207px;font:700 46px/1.18 "Montserrat",sans-serif;color:#fff;letter-spacing:1px}
.hero-sub{left:259px;top:329px;font:400 17px/1.3 "Montserrat",sans-serif;color:#fff;white-space:nowrap}
.hero-sub b{font-weight:700;font-size:18px}
.dots{left:259px;top:400px;display:flex;gap:6px}
.dots span{width:22px;height:4px;border:1px solid #fff}
.dots span.on{background:var(--orange);border-color:var(--orange)}
.ticker{left:258px;top:449px;width:683px;height:37px;background:#fff;display:flex;align-items:center;font:700 8px "Arimo",sans-serif;color:#222;border-bottom:1px solid #e6e6e6}
.ticker .arrow{width:32px;text-align:center;color:#999;font-size:12px}
.ticker .rates{flex:1;display:flex;justify-content:space-between;padding:0 6px}
.up{color:var(--green)} .down{color:var(--red)} .flat{color:var(--orange)}
.card{left:258px;top:486px;width:683px;height:454px;background:#fff;box-shadow:0 1px 2px rgba(0,0,0,.15)}
.welcome-title{left:280px;top:516px;font:700 20px "Arimo",sans-serif;color:var(--ink);white-space:nowrap}
.welcome-text{left:280px;top:548px;width:410px;font:400 10.3px/14.8px "Arimo",sans-serif;color:#222;white-space:nowrap}
.learn{left:279px;top:621px;width:113px;height:30px;background:linear-gradient(#2cb4f0,#138fd0);color:#fff;font:700 9px "Arimo",sans-serif;display:flex;align-items:center;justify-content:center;border:1px solid #0f7db8}
.access{left:705px;top:518px;width:215px;height:132px;background:#333;border:1px solid #222}
.access-head{height:30px;background:linear-gradient(#e05a1c,#b8411a);display:flex;align-items:center;gap:7px;padding-left:11px;color:#fff;font:700 11.5px "Montserrat",sans-serif;letter-spacing:.5px}
.access-field{margin:10px 11px 0;height:19px;background:#fff;font:700 7px "Arimo",sans-serif;color:#888;display:flex;align-items:center;padding-left:11px;border:1px solid #ddd}
.access-foot{display:flex;justify-content:space-between;align-items:center;margin:12px 11px 0}
.access-foot a{color:#ddd;font:400 6.5px "Arimo",sans-serif;text-decoration:underline}
.access-login{background:var(--green);color:#fff;font:700 5px "Arimo",sans-serif;padding:5px 8px}
.feature{top:686px;width:206px;text-align:center}
.feature-photo{width:206px;height:124px;border:1px solid #ccc}
.feature h3{margin-top:13px;font:700 12px "Arimo",sans-serif;color:var(--orange)}
.feature p{margin-top:7px;font:400 8.4px/12.7px "Arimo",sans-serif;color:#444;white-space:nowrap}
.verified{left:0;top:962px;width:1200px;text-align:center;font:700 9px "Arimo",sans-serif;color:#333}
.badges{left:410px;top:984px;width:382px;height:58px;display:flex;align-items:center;justify-content:space-between}
.footer{left:0;top:1063px;width:1200px;height:212px;background:var(--footer)}
.fcol{top:1093px}
.fcol h4{font:700 11px "Arimo",sans-serif;color:var(--orange);margin-bottom:6px}
.fcol ul{list-style:none}
.fcol li{font:400 7.7px/15.3px "Arimo",sans-serif;color:#e8e8e8}
.fcol h4.second{margin-top:22px}
.legal{left:0;top:1275px;width:1200px;height:189px;background:var(--footer-deep)}
.legal-text{left:259px;top:1300px;width:690px;font:400 7.7px/15.4px "Arimo",sans-serif;color:#e6e6e6}
.copyright{left:0;top:1433px;width:1200px;text-align:center;font:400 6.5px "Arimo",sans-serif;color:var(--orange);text-transform:uppercase}
</style>
</head>
<body>
<div class="site">
  <div class="abs topline"></div>
  <header class="abs header"></header>
  <div class="abs brand"><span class="brand-mark"></span><span class="brand-name">Marlowe Capital Group</span></div>
  <a class="abs apply">APPLY NOW</a>
  <nav class="abs nav">
    <a class="active">Home</a>
    <a>About Us<span class="caret">▾</span></a>
    <a>Investments<span class="caret">▾</span></a>
    <a>Funds<span class="caret">▾</span></a>
    <a>Brokerage<span class="caret">▾</span></a>
    <a>Exchange<span class="caret">▾</span></a>
    <a>Accounts<span class="caret">▾</span></a>
    <a>Contact Us</a>
  </nav>

  <section class="abs hero" role="img" aria-label="City skyline with illuminated office towers at night"></section>
  <h1 class="abs hero-title">Financial<br>Management</h1>
  <p class="abs hero-sub">We offer tailored and flexible solutions for banking and<br>financial management that <b>meets your business’s needs.</b></p>
  <div class="abs dots"><span class="on"></span><span></span><span></span><span></span></div>

  <div class="abs ticker">
    <span class="arrow">◀</span>
    <div class="rates">
      <span>GBP / UAH = &nbsp;<span class="up">12.65761 &nbsp;▲</span></span>
      <span>GBP / UCX = &nbsp;<span class="down">4010.06174 &nbsp;▼</span></span>
      <span>GBP / USD = &nbsp;<span class="up">1.55817 &nbsp;▲</span></span>
      <span>GBP / UYU = &nbsp;<span class="up">30.36026 &nbsp;▲</span></span>
      <span>GBP / VEF = &nbsp;<span class="flat">0</span></span>
    </div>
    <span class="arrow">▶</span>
  </div>

  <main class="abs card"></main>
  <h2 class="abs welcome-title">Welcome to Marlowe Capital Group</h2>
  <p class="abs welcome-text">Lorem ipsum dolor sit amet, consectetuer adipiscing elit, sed diam nonummy nibh<br>euismod tincidunt ut laoreet dolore magna aliquam erat volutpat. Ut wisi enim ad<br>minim veniam, quis nostrud exerci tation ullamcorper suscipit lobortis nisl ut aliquip<br>ex ea commodo.</p>
  <a class="abs learn">LEARN MORE</a>

  <form class="abs access">
    <div class="access-head">
      <svg width="9" height="11" viewBox="0 0 9 11"><rect x="0" y="4.5" width="9" height="6.5" fill="#fff"/><path d="M2 4.5V3a2.5 2.5 0 0 1 5 0v1.5" stroke="#fff" stroke-width="1.5" fill="none"/></svg>
      PRIVATE ACCESS
    </div>
    <div class="access-field">Acct. Number</div>
    <div class="access-field">Password</div>
    <div class="access-foot"><a>Forgot acc number/password?</a><span class="access-login">LOG IN TO ACCOUNTS</span></div>
  </form>

  <article class="abs feature" style="left:279px">
    <div class="feature-photo" role="img" aria-label="Hands with a pen reviewing a bar chart report" style="background:linear-gradient(135deg,#f4f4f4,#d8dde0 55%,#9bd0e8)"></div>
    <h3>Management &amp; Strategy</h3>
    <p>Lorem ipsum dolor sit amet, consectetuer adipisc<br>ing elit, sed diam nonummy nibh euismod tincidunt<br>ut laoreet dolore magna aliquam erat volutpat.<br>Ut wisi enim ad minim veniam, quis.</p>
  </article>
  <article class="abs feature" style="left:497px">
    <div class="feature-photo" role="img" aria-label="Two businessmen in suits signing documents" style="background:linear-gradient(135deg,#9fb4cc,#2c3f66 55%,#e8edf3)"></div>
    <h3>Funds</h3>
    <p>Lorem ipsum dolor sit amet, consectetuer adipisc<br>ing elit, sed diam nonummy nibh euismod tincidunt<br>ut laoreet dolore magna aliquam erat volutpat.<br>Ut wisi enim ad minim veniam, quis.</p>
  </article>
  <article class="abs feature" style="left:715px">
    <div class="feature-photo" role="img" aria-label="Golden dollar signs over a currency background" style="background:linear-gradient(135deg,#c98a1a,#f2c24a 45%,#7a4a10)"></div>
    <h3>Currency Exchange</h3>
    <p>Lorem ipsum dolor sit amet, consectetuer adipisc<br>ing elit, sed diam nonummy nibh euismod tincidunt<br>ut laoreet dolore magna aliquam erat volutpat.<br>Ut wisi enim ad minim veniam, quis.</p>
  </article>

  <p class="abs verified">Verified and Protected by</p>
  <div class="abs badges">
    <svg width="72" height="28" role="img" aria-label="Partner badge"><rect width="72" height="28" fill="var(--badge)"/></svg>
    <svg width="92" height="26" role="img" aria-label="Certification badge"><rect width="92" height="26" fill="var(--badge)"/></svg>
    <svg width="56" height="56" role="img" aria-label="Certification badge"><circle cx="28" cy="28" r="27" fill="var(--badge)"/></svg>
    <svg width="82" height="36" role="img" aria-label="Certification badge"><rect x="0" y="4" width="82" height="28" rx="14" fill="var(--badge)"/></svg>
  </div>

  <footer class="abs footer"></footer>
  <div class="abs fcol" style="left:259px"><h4>About Us</h4><ul><li>History</li><li>Expertize</li><li>Identity</li><li>Strategy</li><li>Contact Us</li></ul></div>
  <div class="abs fcol" style="left:368px"><h4>Investments</h4><ul><li>Term Deposits</li><li>Management &amp; Strategy</li><li>Client Relations</li><li>Financial Privacy</li><li>Tax Advice</li><li>Wealth Analysis &amp; Financial Planning</li><li>Active Advisory Group</li><li>Manager Selection Services</li><li>Private Equity</li></ul></div>
  <div class="abs fcol" style="left:563px"><h4>Investments</h4><ul><li>Overview</li><li>Administration</li><li>Funds Security</li><li>Core Security</li><li>Reporting</li><li>Revenue Opportunities</li><li>How It Works?</li><li>Glossary</li></ul></div>
  <div class="abs fcol" style="left:706px"><h4>Currency Exchange</h4><ul><li>Foreign Exchange</li><li>Fx Forward</li><li>Fx Options</li></ul><h4 class="second">Accounts</h4><ul><li>Apply Now</li><li>Private Access</li></ul></div>
  <div class="abs fcol" style="left:873px"><h4>Brokerage</h4><ul><li>Foreign Exchange</li><li>Fx Forward</li><li>Fx Options</li></ul></div>

  <div class="abs legal"></div>
  <p class="abs legal-text">Lorem ipsum dolor sit amet, consectetuer adipiscing elit, sed diam nonummy nibh euismod tincidunt ut laoreet dolore magna aliquam erat volutpat. Ut wisi enim ad minim veniam, quis nostrud exerci tation ullamcorper suscipit lobortis nisl ut aliquip ex ea commodo consequat. Duis autem vel eum iriure dolor in hendrerit in vulputate velit esse molestie conse quat, vel illum dolore eu feugiat nulla facilisis at vero eros et accumsan et iusto odio dignissim qui blandit praesent luptatum zzril delenit augue duis dolore te feugait nulla facilisi. Epsum factorial non deposit quid pro quo hic escorol. Olypian quarrels et gorilla congolium sic ad nauseum. Souvlaki ignitus carborundum e pluribus unum. Defacto lingo est igpay atinlay. Marquee selectus non provisio incongruous feline nolo contendre. Gratuitous octopus niacin, sodium glutimate. Quote meon an estimate et non interruptus stadium. Sic tempus fugit esperanto hiccup estrogen. Glorious baklava ex librus hup hey ad infinitum. Non sequitur condominium facile et geranium incognito.</p>
  <p class="abs copyright">Copyright © 2013 Marlowe Capital Group. All rights reserved.</p>
</div>
</body>
</html>
```